social interest sharing site needs a web site design

we need a web site design for a social web platform.
the site is one page(main page), that is split into 3 sections
each section is a different color(red,green and blue)
and a user can choose to share each of the sections.
any section/color will contain boxes , each box can contain different media types.

the media types:
* list of URLS
* list of articles including title + image + description
* list of videos
* thumbnails of images
* calender
* list of emails

the main content will look like corkboardly layout
multiple boxes each box can contain different type of content as described above

each color is a different tab
each tab will have layout like corkboardly
Updates

please read the last description update.
and i uploaded an image that can explain the requirements better

thanks
Oren
 

Industry/Entity Type

Media

```html
<!DOCTYPE html>
<html lang="en">
<head>
<meta charset="utf-8">
<title>tintboard.</title>
<link href="https://fonts.googleapis.com/css2?family=Nunito:wght@700;800&family=Open+Sans:wght@400;600;700&family=Dancing+Script:wght@600&display=swap" rel="stylesheet">
<style>
  :root{
    --ink:#33363b;
    --white:#ffffff;
    --soft-grey:#ebe8e5;
    --red:#fd7b73;
    --red-band:#e2655f;
    --green:#2ddfc2;
    --green-band:#22c9ae;
    --blue:#3f5c86;
    --blue-band:#344f76;
    --ghost:rgba(255,255,255,.28);
  }
  *{box-sizing:border-box;margin:0;padding:0}
  html,body{width:1200px;height:675px;overflow:hidden;background:var(--white);font-family:"Open Sans",sans-serif}
  .page{position:relative;width:1200px;height:675px;overflow:hidden}
  .site-title{position:absolute;top:12px;left:0;width:100%;text-align:center;font-family:"Nunito",sans-serif;font-weight:800;font-size:54px;letter-spacing:1px;color:var(--ink);line-height:60px}
  .share-row{position:absolute;display:flex;gap:8px}
  .share-row span{width:44px;height:44px;border-radius:50%;display:flex;align-items:center;justify-content:center;font:700 8px "Open Sans",sans-serif;color:var(--white);text-transform:lowercase}
  .header-share{top:75px;left:422px}
  .header-share span{background:var(--soft-grey)}
  .mail{position:absolute;left:1100px;top:65px;width:81px;height:54px}
  .column{position:absolute;top:135px;width:400px;height:502px;overflow:hidden}
  .column::before{content:"";position:absolute;top:0;left:0;right:0;height:12px;background:var(--band)}
  .col-red{left:0;background:var(--red);--band:var(--red-band)}
  .col-green{left:400px;background:var(--green);--band:var(--green-band)}
  .col-blue{left:800px;background:var(--blue);--band:var(--blue-band)}
  .column .share-row{top:30px;left:20px}
  .column .share-row span{background:var(--ghost)}
  .column .share-row span.active{background:var(--white);color:var(--red)}
  .scrollbar{position:absolute;left:383px;top:12px;width:14px;height:490px;background:rgba(0,0,0,.06)}
  .scrollbar::after{content:"";position:absolute;left:0;top:13px;width:14px;height:24px;border-radius:7px;background:var(--white)}
  .type{position:absolute;width:20px;height:20px}
  .box{position:absolute;overflow:hidden}
  .photo-grid{display:grid;gap:1px}
  .photo-grid div{background:var(--c)}
  .article{background:var(--white)}
  .grass-title{position:absolute;left:0;right:0;bottom:0;height:58px;text-align:center;color:var(--ink);padding-top:7px}
  .grass-title b{display:block;font:700 17px "Open Sans",sans-serif;line-height:19px}
  .grass-title small{display:block;font:600 10px "Open Sans",sans-serif;line-height:14px}
  .url-list{position:absolute;left:427px;top:443px;list-style:none;color:var(--white);font-weight:700;font-size:19px;line-height:31px}
  .url-list li{position:absolute;white-space:nowrap}
  .url-list small{font-size:14px}
  .calendar{display:flex;gap:2px}
  .calendar div{width:23px;height:24px;background:var(--white);opacity:.92}
  .flowers-title{position:absolute;left:0;right:0;top:184px;text-align:center;color:var(--ink)}
  .flowers-title .small{font:600 26px "Open Sans",sans-serif;line-height:30px;letter-spacing:.5px}
  .flowers-title .big{font:700 58px "Open Sans",sans-serif;line-height:58px;letter-spacing:1px}
  .flowers-title .script{font:600 26px "Dancing Script",cursive;line-height:26px}
  .email{position:absolute;left:1012px;top:625px;color:var(--white);font-weight:700;font-size:15px}
  .footer-bar{position:absolute;left:0;top:637px;width:1200px;height:38px;background:var(--white);box-shadow:0 -3px 6px rgba(0,0,0,.12)}
</style>
</head>
<body>
<div class="page">
  <header>
    <h1 class="site-title">tintboard.</h1>
    <nav class="share-row header-share" aria-label="Share">
      <span>Folio</span><span>Chirper</span><span>Linkwise</span><span>Newsline</span><span>Searchly</span><span>Threadly</span><span>Yodel</span>
    </nav>
    <svg class="mail" viewBox="0 0 81 54" aria-label="Contact"><rect width="81" height="54" rx="3" fill="#ebe8e5"/><polyline points="6,6 40.5,40 75,6" fill="none" stroke="#fff" stroke-width="3"/></svg>
  </header>

  <section class="column col-red">
    <div class="share-row"><span class="active">Folio</span><span>Chirper</span><span>Linkwise</span><span>Newsline</span><span>Searchly</span><span>Threadly</span><span>Yodel</span></div>
    <div class="scrollbar"></div>

    <svg class="type" style="left:17px;top:97px" viewBox="0 0 20 20"><rect x="1" y="1" width="18" height="18" fill="none" stroke="#fff" stroke-width="2"/><polyline points="3,16 8,9 11,13 13,11 17,16" fill="none" stroke="#fff" stroke-width="1.5"/><circle cx="14" cy="6" r="1.6" fill="#fff"/></svg>
    <div class="box photo-grid" style="left:16px;top:121px;width:364px;height:139px;grid-template-columns:repeat(5,1fr);grid-template-rows:1fr 1fr" role="img" aria-label="Gallery of ten nature photographs">
      <div style="--c:#c55a6c"></div><div style="--c:#1d3a73"></div><div style="--c:#a9c6c4"></div><div style="--c:#b7a15f"></div><div style="--c:#a8763a"></div>
      <div style="--c:#8f9a6b"></div><div style="--c:#aeb8bb"></div><div style="--c:#8c9a55"></div><div style="--c:#c9a57d"></div><div style="--c:#5f6ea0"></div>
    </div>

    <svg class="type" style="left:17px;top:279px" viewBox="0 0 20 20"><rect x="1" y="1" width="18" height="18" fill="none" stroke="#fff" stroke-width="2"/><line x1="10" y1="3" x2="10" y2="17" stroke="#fff" stroke-width="1.5"/><path d="M4 6h4M4 9h4M4 12h4M12 6h4M12 9h4M12 12h4" stroke="#fff"/></svg>
    <article class="box article" style="left:15px;top:301px;width:175px;height:137px">
      <div style="height:80px;background:linear-gradient(180deg,#5b5b5b,#b8b8b8)" role="img" aria-label="Black and white photo of grass stems"></div>
      <div class="grass-title"><b>GRASS:</b><small>DANGEROUS DRUG,</small><small>OR NATURES CARPET?</small></div>
    </article>

    <svg class="type" style="left:207px;top:279px" viewBox="0 0 20 20"><rect x="1" y="1" width="18" height="18" fill="none" stroke="#fff" stroke-width="2"/><polyline points="3,16 8,9 11,13 13,11 17,16" fill="none" stroke="#fff" stroke-width="1.5"/><circle cx="14" cy="6" r="1.6" fill="#fff"/></svg>
    <div class="box" style="left:205px;top:301px;width:175px;height:137px;background:linear-gradient(180deg,#e6c7ef,#b58ec6 70%,#a07ab5)" role="img" aria-label="Misty purple forest photograph"></div>

    <svg class="type" style="left:17px;top:455px" viewBox="0 0 20 20"><rect x="1" y="3" width="18" height="14" fill="none" stroke="#fff" stroke-width="2"/><path d="M4 3v14M16 3v14" stroke="#fff" stroke-width="1.5" stroke-dasharray="2 2"/></svg>
    <div class="box" style="left:15px;top:477px;width:365px;height:40px;background:linear-gradient(90deg,#0f3b3c,#24564f 50%,#0d3436)" role="img" aria-label="Video thumbnail of a flower"></div>
  </section>

  <section class="column col-green">
    <div class="share-row"><span>Folio</span><span>Chirper</span><span>Linkwise</span><span>Newsline</span><span>Searchly</span><span>Threadly</span><span>Yodel</span></div>

    <svg class="type" style="left:20px;top:97px" viewBox="0 0 20 20"><rect x="1" y="3" width="18" height="14" fill="none" stroke="#fff" stroke-width="2"/><path d="M4 3v14M16 3v14" stroke="#fff" stroke-width="1.5" stroke-dasharray="2 2"/></svg>
    <div class="box" style="left:17px;top:121px;width:176px;height:139px;background:linear-gradient(135deg,#4a4540,#2a2522 60%,#55504a)" role="img" aria-label="Video thumbnail of a person speaking">
      <svg style="position:absolute;left:66px;top:48px" width="44" height="34" viewBox="0 0 44 34"><rect width="44" height="34" rx="8" fill="#1c1c1c" opacity=".85"/><polygon points="17,10 30,17 17,24" fill="#fff"/></svg>
    </div>

    <svg class="type" style="left:20px;top:278px" viewBox="0 0 20 20"><rect x="1" y="3" width="18" height="14" fill="none" stroke="#fff" stroke-width="2"/><line x1="1" y1="7" x2="19" y2="7" stroke="#fff" stroke-width="1.5"/><text x="10" y="15" font-size="5" fill="#fff" text-anchor="middle" font-family="Open Sans, sans-serif" font-weight="700">www</text></svg>

    <svg class="type" style="left:208px;top:97px" viewBox="0 0 20 20"><rect x="1" y="1" width="18" height="18" fill="none" stroke="#fff" stroke-width="2"/><polyline points="3,16 8,9 11,13 13,11 17,16" fill="none" stroke="#fff" stroke-width="1.5"/><circle cx="14" cy="6" r="1.6" fill="#fff"/></svg>
    <div class="box photo-grid" style="left:206px;top:121px;width:176px;height:317px;grid-template-columns:1fr 1fr;grid-template-rows:repeat(4,1fr)" role="img" aria-label="Gallery of eight landscape photographs">
      <div style="--c:#b3b088"></div><div style="--c:#c6cdd2"></div>
      <div style="--c:#587a6c"></div><div style="--c:#a9b3ab"></div>
      <div style="--c:#8f8374"></div><div style="--c:#a986ae"></div>
      <div style="--c:#4f8a3f"></div><div style="--c:#6d92c9"></div>
    </div>

    <svg class="type" style="left:208px;top:455px" viewBox="0 0 20 20"><rect x="1" y="1" width="18" height="18" fill="none" stroke="#fff" stroke-width="2"/><text x="10" y="12" font-size="9" fill="#fff" text-anchor="middle" font-family="Open Sans, sans-serif" font-weight="700">1</text><text x="10" y="17" font-size="3" fill="#fff" text-anchor="middle" font-family="Open Sans, sans-serif">june</text></svg>
    <div class="box calendar" style="left:208px;top:478px;width:176px;height:24px" aria-label="Calendar"><div></div><div></div><div></div><div></div><div></div><div></div><div></div></div>
  </section>

  <ul class="url-list">
    <li style="top:0">•leafyo<small>.com</small></li>
    <li style="top:31px">•leafycity<small>.com</small></li>
    <li style="top:62px">•leafytown<small>.org</small></li>
    <li style="top:93px">•leafyo<small>.com</small></li>
    <li style="top:124px">•leafycity<small>.com</small></li>
    <li style="top:155px">•leafytown<small>.org</small></li>
  </ul>

  <section class="column col-blue">
    <div class="share-row"><span>Folio</span><span>Chirper</span><span>Linkwise</span><span>Newsline</span><span>Searchly</span><span>Threadly</span><span>Yodel</span></div>

    <svg class="type" style="left:22px;top:97px" viewBox="0 0 20 20"><rect x="1" y="1" width="18" height="18" fill="none" stroke="#fff" stroke-width="2"/><line x1="10" y1="3" x2="10" y2="17" stroke="#fff" stroke-width="1.5"/><path d="M4 6h4M4 9h4M4 12h4M12 6h4M12 9h4M12 12h4" stroke="#fff"/></svg>
    <article class="box article" style="left:19px;top:121px;width:364px;height:317px">
      <div style="height:168px;background:linear-gradient(180deg,#9aa870,#b9a67e 55%,#a8a06c)" role="img" aria-label="Photo of pink poppy flowers"></div>
      <div class="flowers-title">
        <div class="small">HOW TO EAT</div>
        <div class="big">FLOWERS</div>
        <div class="script">like a boss</div>
      </div>
    </article>

    <svg class="type" style="left:22px;top:455px" viewBox="0 0 20 20"><rect x="1" y="1" width="18" height="18" fill="none" stroke="#fff" stroke-width="2"/><text x="10" y="12" font-size="9" fill="#fff" text-anchor="middle" font-family="Open Sans, sans-serif" font-weight="700">1</text><text x="10" y="17" font-size="3" fill="#fff" text-anchor="middle" font-family="Open Sans, sans-serif">june</text></svg>
    <div class="box calendar" style="left:20px;top:478px;width:176px;height:24px" aria-label="Calendar"><div></div><div></div><div></div><div></div><div></div><div></div><div></div></div>

    <svg class="type" style="left:210px;top:455px" viewBox="0 0 20 20"><rect x="1" y="1" width="18" height="18" fill="none" stroke="#fff" stroke-width="2"/><text x="10" y="14" font-size="12" fill="#fff" text-anchor="middle" font-family="Open Sans, sans-serif" font-weight="700">@</text></svg>
  </section>

  <div class="email">•mix@leafyo.com</div>

  <div class="footer-bar"></div>
</div>
</body>
</html>
```